Real Estate Company / Capital Needs Cards!

need business cards designed using the logos that were just designed by sketchhive.

Reason: per designers request deadline extended 1 day…thank you.

Target Market(s)

Investors and clients looking to purchase real estate or invest in the business.

Industry/Entity Type

Business

Requirements
Must have
• two designs - one for the real estate logo and one for the capital logo, similar but slightly different.
Nice to have
• something to make it pop (perhaps on the back)
Should not have
• much color

```html
<!DOCTYPE html>
<html lang="en">
<head>
<meta charset="utf-8">
<title>Lumen Business Cards</title>
<link href="https://fonts.googleapis.com/css2?family=Cinzel:wght@400;600;700&family=Crimson+Text:wght@400;600&display=swap" rel="stylesheet">
<style>
  :root {
    --backdrop: #2b2b2d;
    --ink: #111214;
    --panel-dark: #1b1d20;
    --panel-mid: #2a2d31;
    --paper: #ffffff;
    --silver: #e6e6e6;
    --silver-dim: #bdbdbd;
    --grey-text: #555555;
  }
  * { margin: 0; padding: 0; box-sizing: border-box; }
  html, body { width: 1200px; height: 871px; overflow: hidden; }
  body {
    background: var(--backdrop);
    position: relative;
    font-family: "Crimson Text", Georgia, serif;
  }
  .card {
    position: absolute;
    left: 250px;
    width: 700px;
    height: 400px;
    background: var(--paper);
    overflow: hidden;
    box-shadow: 0 6px 18px rgba(0,0,0,.45);
  }
  .card--front { top: 24px; }
  .card--back { top: 447px; }

  .front-panel { position: absolute; inset: 0; }

  .brand {
    position: absolute;
    display: flex;
    align-items: center;
    gap: 14px;
  }
  .brand__mark { background: var(--silver); }
  .brand__name {
    font-family: "Cinzel", "Times New Roman", serif;
    font-weight: 400;
    line-height: 1;
  }
  .brand__name .line-main { display: block; letter-spacing: 3px; }
  .brand__name .line-sub { display: block; letter-spacing: 2.5px; margin-top: 4px; }

  .card--front .brand { top: 72px; right: 70px; }
  .card--front .brand__mark { width: 62px; height: 62px; }
  .card--front .brand__name { color: var(--silver); }
  .card--front .line-main { font-size: 44px; }
  .card--front .line-sub { font-size: 16px; }

  .holder {
    position: absolute;
    left: 30px;
    top: 210px;
  }
  .holder__name {
    font-family: "Cinzel", "Times New Roman", serif;
    font-weight: 700;
    font-size: 24px;
    color: var(--paper);
    letter-spacing: 1px;
  }
  .holder__title {
    font-family: "Cinzel", "Times New Roman", serif;
    font-size: 13px;
    color: var(--ink);
    letter-spacing: 1px;
    margin-top: 6px;
  }

  .contact {
    position: absolute;
    font-size: 17px;
    color: var(--ink);
  }
  .contact__key {
    display: block;
    width: 20px;
    height: 20px;
    background: var(--ink);
    color: var(--paper);
    font-family: "Cinzel", serif;
    font-weight: 700;
    font-size: 12px;
    line-height: 20px;
    text-align: center;
    margin-bottom: 3px;
  }
  .contact--email { left: 300px; top: 240px; }
  .contact--web { left: 300px; top: 300px; }
  .contact--fax { left: 500px; top: 208px; }
  .contact--phone { left: 500px; top: 262px; }
  .contact--address { left: 30px; top: 330px; }

  .card--back .brand {
    top: 120px;
    left: 50%;
    transform: translateX(-50%);
  }
  .card--back .brand__mark { width: 52px; height: 52px; background: var(--grey-text); }
  .card--back .brand__name { color: var(--grey-text); }
  .card--back .line-main { font-size: 38px; }
  .card--back .line-sub { font-size: 13px; }
  .back-web {
    position: absolute;
    top: 196px;
    width: 100%;
    text-align: center;
    font-size: 17px;
    color: var(--ink);
  }
  .back-blurb {
    position: absolute;
    top: 290px;
    width: 100%;
    text-align: center;
    font-size: 15px;
    line-height: 1.4;
    color: var(--ink);
  }
</style>
</head>
<body>

<section class="card card--front" aria-label="Lumen Real Estate business card">
  <svg class="front-panel" width="700" height="400" viewBox="0 0 700 400" aria-hidden="true">
    <defs>
      <linearGradient id="panelShade" x1="0" y1="0" x2="1" y2="1">
        <stop offset="0" stop-color="var(--panel-mid)"/>
        <stop offset="1" stop-color="var(--panel-dark)"/>
      </linearGradient>
    </defs>
    <polygon points="0,0 700,0 700,196 312,196 284,232 0,232" fill="url(#panelShade)"/>
  </svg>

  <div class="brand">
    <span class="brand__mark"></span>
    <span class="brand__name">
      <span class="line-main">LUMEN</span>
      <span class="line-sub">REAL ESTATE</span>
    </span>
  </div>

  <div class="holder">
    <div class="holder__name">YOUR NAME</div>
    <div class="holder__title">JOB TITLE</div>
  </div>

  <div class="contact contact--email"><span class="contact__key">E</span>info@yoursite.com</div>
  <div class="contact contact--web"><span class="contact__key">W</span>www.yoursite.com</div>
  <div class="contact contact--fax"><span class="contact__key">F</span>613 555 0145</div>
  <div class="contact contact--phone"><span class="contact__key">P</span>613 555 0145</div>
  <div class="contact contact--address"><span class="contact__key">A</span>123 sdaf rd, sdfaf, asdf</div>
</section>

<section class="card card--back" aria-label="Lumen Capital business card">
  <div class="brand">
    <span class="brand__mark"></span>
    <span class="brand__name">
      <span class="line-main">LUMEN</span>
      <span class="line-sub">CAPITAL, LLC</span>
    </span>
  </div>
  <div class="back-web">www.yoursite.com</div>
  <p class="back-blurb">Lorem ipsum dolor sit amet, consectetur adipiscing elit.<br>Integer pulvinar.</p>
</section>

</body>
</html>
```